Harbour Lantern Fliers and logo design

We need to design a product logo and some informational fliers for a summit quest.
I have attached our Harbour Lantern logo - colours need to be complimentary but not the same, we would like fresh, funky but still professional. We generally communicate in a fairly casual way to reach our market. (We don't like boring)
Clear and simple - not too busy
images are good but not actual photos
Here is our website to give you an idea www.harbourlantern-example.co.nz
The flier is a 3 page document.
The logo is to say Summit Quest. The challenge is based on exercise, connecting with people, giving, learning and taking notice (The 4 keys to brightwater) Once agin the logo needs to be complementary but not the same.
The Harbour lantern logo needs to be on the fliers but the summit quest logo is separate.
Thanks very much!!

```html
<!DOCTYPE html>
<html lang="en">
<head>
<meta charset="utf-8">
<title>Stress Buster! – Harbour Lantern</title>
<link href="https://fonts.googleapis.com/css2?family=Oswald:wght@500;600&family=Open+Sans:wght@400;600&family=Varela+Round&display=swap" rel="stylesheet">
<style>
  :root{
    --green:#47a63f;
    --teal:#4dbfa6;
    --teal-text:#2fae93;
    --red:#e8452d;
    --stop-red:#e31e24;
    --ink:#2b2b2b;
    --white:#ffffff;
  }
  *{box-sizing:border-box;margin:0;padding:0}
  html,body{width:800px;height:1200px;overflow:hidden;background:#fff}
  .flyer{position:relative;width:800px;height:1200px;background:var(--white);font-family:"Open Sans",sans-serif;color:var(--ink)}
  .hero-image{position:absolute;left:0;top:0;width:800px;height:440px;
    background:linear-gradient(180deg,#f4f4f4 0%,#e2d6cc 45%,#b9a699 75%,#8e8f96 100%)}
  .band{position:absolute;left:0;width:418px;height:14px;background:var(--teal)}
  .band--top{top:438px}
  .band--bottom{bottom:0;height:18px}

  .brand{position:absolute;left:0;width:418px;top:492px;display:flex;align-items:center;justify-content:center;gap:10px}
  .brand-dot{width:20px;height:20px;border-radius:50%;background:var(--teal-text)}
  .brand-name{font-family:"Varela Round",sans-serif;font-size:32px;line-height:1;color:var(--teal-text)}

  .intro{position:absolute;left:24px;top:596px;width:372px}
  .intro h1{font-family:"Oswald",sans-serif;font-weight:600;font-size:40px;line-height:1.1;color:var(--red)}
  .intro .tagline{font-family:"Oswald",sans-serif;font-weight:500;font-size:18px;line-height:1.4;color:var(--teal-text);margin-top:6px;white-space:nowrap}
  .intro .copy{margin-top:20px}
  .intro .copy p{font-size:12.4px;line-height:1.45;text-align:justify;margin-bottom:14px}

  .stop-panel{position:absolute;left:418px;top:290px;width:382px;height:910px;background:var(--green);color:var(--white)}
  .stop-sign{position:absolute;left:20px;top:58px;width:156px;height:156px}
  .stop-steps-title{position:absolute;left:194px;top:62px;font-family:"Oswald",sans-serif;font-weight:500;font-size:28px;line-height:1.6;letter-spacing:.3px}
  .step{position:absolute;left:20px;width:344px}
  .step-badge{position:absolute;left:0;top:0;width:52px;height:52px}
  .step-body{margin-left:80px}
  .step h2{font-size:17px;font-weight:600;line-height:1.2}
  .step p{font-size:12px;line-height:1.35;margin-top:4px}
  .step h3{font-size:13.5px;font-weight:600;margin-top:18px}
</style>
</head>
<body>
<main class="flyer">
  <div class="hero-image" role="img" aria-label="Image of a cheering group of colleagues with arms raised"></div>
  <div class="band band--top"></div>

  <div class="brand">
    <span class="brand-dot"></span>
    <span class="brand-name">harbour lantern</span>
  </div>

  <section class="intro">
    <h1>Stress Buster!</h1>
    <p class="tagline">We cannot control what happens to us in life,<br>but we can change the way we react</p>
    <div class="copy">
      <p>Stress happens because we are allowing fear, anger, disappointment and a host of other negative emotions to navigate our actions. By becoming aware of these emotions and allowing them to simply be, we can begin to gain control of how we react and respond to stressful situations.</p>
      <p>Our experience is always changing. Without awareness, mental patterns related to what we fear and what upsets us make life harder.</p>
      <p>S.T.O.P is a powerful, yet surprisingly basic strategy that helps you to be focused, alert, relaxed and at your emotional best when stressful moments present themselves in your life.</p>
      <p>Simply put, it's a four-step checklist to use anytime you want to ground yourself and get some insight into whatever is going on. The whole idea behind it is that by taking a very brief break—even less than one minute—you can determine the very best action to take in the moment.</p>
    </div>
  </section>
  <div class="band band--bottom"></div>

  <section class="stop-panel">
    <svg class="stop-sign" viewBox="0 0 100 100" aria-hidden="true">
      <polygon points="29,2 71,2 98,29 98,71 71,98 29,98 2,71 2,29" fill="#fff"/>
      <polygon points="31,7 69,7 93,31 93,69 69,93 31,93 7,69 7,31" fill="var(--stop-red)"/>
      <text x="50" y="62" text-anchor="middle" font-family="Oswald,sans-serif" font-weight="600" font-size="32" fill="#fff">STOP</text>
    </svg>
    <div class="stop-steps-title">STOP<br>TAKE A BREATH<br>OBSERVE<br>PROCEED</div>

    <div class="step" style="top:306px">
      <svg class="step-badge" viewBox="0 0 100 100" aria-hidden="true"><polygon points="29,2 71,2 98,29 98,71 71,98 29,98 2,71 2,29" fill="#fff"/><polygon points="31,8 69,8 92,31 92,69 69,92 31,92 8,69 8,31" fill="var(--stop-red)"/><text x="50" y="68" text-anchor="middle" font-family="Oswald,sans-serif" font-weight="600" font-size="46" fill="#fff">S</text></svg>
      <div class="step-body"><h2>Stop</h2><p>Stop what you are doing: Press the pause button on your thoughts and actions.</p></div>
    </div>

    <div class="step" style="top:394px">
      <svg class="step-badge" viewBox="0 0 100 100" aria-hidden="true"><polygon points="29,2 71,2 98,29 98,71 71,98 29,98 2,71 2,29" fill="#fff"/><polygon points="31,8 69,8 92,31 92,69 69,92 31,92 8,69 8,31" fill="var(--stop-red)"/><text x="50" y="68" text-anchor="middle" font-family="Oswald,sans-serif" font-weight="600" font-size="46" fill="#fff">T</text></svg>
      <div class="step-body"><h2>Take</h2><p>Take a few deep breaths to centre yourself and bring yourself fully into the present moment.</p></div>
    </div>

    <div class="step" style="top:492px">
      <svg class="step-badge" viewBox="0 0 100 100" aria-hidden="true"><polygon points="29,2 71,2 98,29 98,71 71,98 29,98 2,71 2,29" fill="#fff"/><polygon points="31,8 69,8 92,31 92,69 69,92 31,92 8,69 8,31" fill="var(--stop-red)"/><text x="50" y="68" text-anchor="middle" font-family="Oswald,sans-serif" font-weight="600" font-size="46" fill="#fff">O</text></svg>
      <div class="step-body">
        <h2>Observe</h2><p>Observe what is going on with your:</p>
        <h3>Body</h3><p>What physical sensations are you aware of (touch, sight, hearing, taste, smell)?</p>
        <h3>Emotions</h3><p>What are you feeling right now?</p>
        <h3>Mind</h3><p>What assumptions are your making about your feelings? What is the story you're telling yourself about why you are having them?</p>
      </div>
    </div>

    <div class="step" style="top:810px">
      <svg class="step-badge" viewBox="0 0 100 100" aria-hidden="true"><polygon points="29,2 71,2 98,29 98,71 71,98 29,98 2,71 2,29" fill="#fff"/><polygon points="31,8 69,8 92,31 92,69 69,92 31,92 8,69 8,31" fill="var(--stop-red)"/><text x="50" y="68" text-anchor="middle" font-family="Oswald,sans-serif" font-weight="600" font-size="46" fill="#fff">P</text></svg>
      <div class="step-body"><h2>Proceed</h2><p>Proceed with whatever you were doing, making a conscious, intentional choice to incorporate what you just learned.</p></div>
    </div>
  </section>
</main>
</body>
</html>
```